Searchable website that will contain information about sites for Velmora Trade Hub.

Once a search is performed the website will show the following information per site:
Title, Description, Screenshot of the site. I'm thinking three items per row.

Number of Pages Required

1 page

Font styles to use
Sans Serif

Colors
ffffff
3176b5

```html
<!DOCTYPE html>
<html lang="en">
<head>
<meta charset="utf-8">
<title>Velmora Trade Hub</title>
<link rel="stylesheet" href="https://fonts.googleapis.com/css2?family=Poppins:wght@400;500;600;700&family=Open+Sans:wght@400;600;700&display=swap">
<style>
:root{
  --blue:#3176b5;
  --blue-dark:#2a63a3;
  --white:#ffffff;
  --ink:#1b1b1b;
  --muted:#555b63;
  --soft:#f4f2f2;
  --line:#c9c9c9;
  --faint:#e3e3e3;
}
*{box-sizing:border-box;margin:0;padding:0}
html,body{width:1200px;height:3982px;overflow:hidden}
body{position:relative;background:var(--white);font-family:"Open Sans",Arial,sans-serif;color:var(--ink)}
.abs{position:absolute}
.heading{font-family:"Poppins",Arial,sans-serif;font-weight:700;font-size:24px;text-align:center;width:1200px;left:0;letter-spacing:.3px}
.rule{left:577px;width:46px;height:3px;background:var(--line)}
/* hero */
.hero{left:0;top:0;width:1200px;height:645px;background:linear-gradient(135deg,#5b4a3f 0%,#3c3430 45%,#6a6260 70%,#2c2828 100%)}
.hero-shade{left:0;top:0;width:1200px;height:645px;background:rgba(20,15,12,.35)}
.brand{left:132px;top:28px;color:var(--white);font-family:"Poppins",Arial,sans-serif;font-weight:700;font-size:25px;letter-spacing:.3px}
.nav{right:132px;top:34px;display:flex;gap:30px}
.nav a{color:var(--white);text-decoration:none;font-family:"Poppins",Arial,sans-serif;font-weight:600;font-size:14px}
.hero-title{left:0;width:1200px;top:245px;text-align:center;color:var(--white);font-family:"Poppins",Arial,sans-serif;font-weight:600;font-size:44px}
.search{left:366px;top:352px;width:484px;height:52px;border:3px solid var(--white);background:rgba(40,34,30,.55);display:flex;align-items:center}
.search-label{flex:1;color:var(--white);font-size:16px;font-weight:600;display:flex;align-items:center;gap:12px;padding-left:22px}
.search-btn{width:104px;height:40px;margin-right:3px;background:var(--blue);color:var(--white);font-family:"Poppins",Arial,sans-serif;font-weight:600;font-size:16px;display:flex;align-items:center;justify-content:center}
/* list */
.list-band{left:0;top:645px;width:1200px;height:1152px;background:var(--soft)}
.card{width:284px;background:var(--white);box-shadow:0 1px 6px rgba(0,0,0,.08)}
.shot{width:284px;height:207px;display:block}
.card-body{padding:24px 28px 0}
.card-title{font-family:"Poppins",Arial,sans-serif;font-weight:700;font-size:15px;margin-bottom:12px}
.card-text{font-size:13px;line-height:18px;color:var(--muted)}
.btn{display:inline-block;background:var(--blue);color:var(--white);font-family:"Poppins",Arial,sans-serif;font-weight:700;font-size:12px;padding:5px 16px;margin-top:22px}
.view-all{left:483px;top:1710px;width:232px;height:36px;background:var(--blue);color:var(--white);font-family:"Poppins",Arial,sans-serif;font-weight:700;font-size:14px;display:flex;align-items:center;justify-content:center}
/* welcome */
.welcome-kicker{left:0;width:1200px;top:1872px;text-align:center;font-family:"Poppins",Arial,sans-serif;font-size:18px}
.welcome-name{left:0;width:1200px;top:1900px;text-align:center;font-family:"Poppins",Arial,sans-serif;font-weight:700;font-size:32px;color:var(--blue)}
.welcome-text{left:350px;width:500px;top:2012px;text-align:center;font-size:15px;line-height:22px;color:var(--muted)}
.feature{width:250px;display:flex;gap:18px;align-items:flex-start}
.feature-title{font-family:"Poppins",Arial,sans-serif;font-weight:500;font-size:15px;margin:2px 0 6px}
.feature-text{font-size:12px;line-height:17px;color:var(--muted)}
/* steps */
.steps-band{left:0;top:2347px;width:1200px;height:510px;background:var(--soft)}
.step{width:298px;text-align:center}
.step-art{width:80px;height:70px;margin:0 auto;border-radius:8px;background:linear-gradient(160deg,#4f86c0,#2c5e98)}
.step-title{font-family:"Poppins",Arial,sans-serif;font-weight:600;font-size:15px;margin-top:46px}
.step-text{font-size:13px;line-height:18px;color:var(--muted);width:210px;margin:12px auto 0}
.step-num{font-family:"Poppins",Arial,sans-serif;font-weight:600;font-size:44px;color:var(--faint);margin-top:4px;line-height:48px}
.step-divider{width:1px;height:224px;top:2548px;background:var(--line)}
/* posts */
.post{width:284px;height:425px;background:var(--soft)}
.post .shot{height:200px}
/* footer */
.footer{left:0;top:3603px;width:1200px;height:379px;background:var(--blue);color:var(--white)}
.f-brand{left:130px;top:138px;font-family:"Poppins",Arial,sans-serif;font-weight:700;font-size:25px}
.f-head{font-family:"Poppins",Arial,sans-serif;font-weight:600;font-size:12px;letter-spacing:.4px}
.f-row{display:flex;gap:14px;font-size:12px;line-height:17px;align-items:flex-start}
.f-menu{font-size:12px;line-height:17px}
.f-social{display:flex;align-items:center;gap:12px;font-size:12px}
.dot{width:24px;height:24px;border-radius:50%;background:var(--white)}
.f-line{left:0;top:312px;width:1200px;height:1px;background:rgba(255,255,255,.25)}
.copy{left:0;width:1200px;top:322px;text-align:center;font-size:11px}
</style>
</head>
<body>

<!-- hero -->
<div class="abs hero" role="img" aria-label="Photo of a person working on a laptop at a desk"></div>
<div class="abs hero-shade"></div>
<div class="abs brand">VELMORA TRADE HUB</div>
<nav class="abs nav"><a>HOME</a><a>ABOUT US</a><a>SERVICES</a><a>ENTREPRENEURS</a><a>BLOG</a><a>CONTACT US</a></nav>
<h1 class="abs hero-title">Online Entrepreneurs</h1>
<div class="abs search">
  <div class="search-label">
    <svg width="14" height="14" viewBox="0 0 14 14"><circle cx="6" cy="6" r="4.5" fill="none" stroke="#fff" stroke-width="2"/><line x1="9.5" y1="9.5" x2="13" y2="13" stroke="#fff" stroke-width="2"/></svg>
    Search Entrepreneurs
  </div>
  <div class="search-btn">SEARCH</div>
</div>

<!-- list -->
<div class="abs list-band"></div>
<h2 class="abs heading" style="top:703px">LIST OF ENTREPRENEURS</h2>
<div class="abs rule" style="top:756px"></div>

<div class="abs card" style="left:159px;top:815px;height:414px">
  <div class="shot" role="img" aria-label="Screenshot of a listed business website with city skyline banner" style="background:linear-gradient(180deg,#e9eef5 0 18%,#3b4f86 18% 55%,#f5f5f5 55%)"></div>
  <div class="card-body"><div class="card-title">LOREM IPSUM IS SIMPLY DUMMY</div><div class="card-text">Sed ut perspiciatis unde omnis iste natus error sit voluptatem accusantium dolore mque laudantium aut odit aut fugit, sed quia consequ</div><span class="btn">READ MORE</span></div>
</div>
<div class="abs card" style="left:462px;top:815px;height:414px">
  <div class="shot" role="img" aria-label="Screenshot of a listed business website with teal header" style="background:linear-gradient(180deg,#2fa39b 0 45%,#f4f4f4 45%)"></div>
  <div class="card-body"><div class="card-title">LOREM IPSUM IS SIMPLY DUMMY</div><div class="card-text">Sed ut perspiciatis unde omnis iste natus error sit voluptatem accusantium dolore mque laudantium aut odit aut fugit, sed quia consequ</div><span class="btn">READ MORE</span></div>
</div>
<div class="abs card" style="left:765px;top:815px;height:414px">
  <div class="shot" role="img" aria-label="Screenshot of a listed business website with sunset photo" style="background:linear-gradient(180deg,#f6d48a 0 60%,#ececec 60%)"></div>
  <div class="card-body"><div class="card-title">LOREM IPSUM IS SIMPLY DUMMY</div><div class="card-text">Sed ut perspiciatis unde omnis iste natus error sit voluptatem accusantium dolore mque laudantium aut odit aut fugit, sed quia consequ</div><span class="btn">READ MORE</span></div>
</div>

<div class="abs card" style="left:159px;top:1253px;height:412px">
  <div class="shot" role="img" aria-label="Screenshot of a listed business website with gold banner" style="background:linear-gradient(180deg,#f2f2f2 0 18%,#d7a12a 18% 48%,#f7f7f7 48% 80%,#2e64b0 80%)"></div>
  <div class="card-body"><div class="card-title">LOREM IPSUM IS SIMPLY DUMMY</div><div class="card-text">Sed ut perspiciatis unde omnis iste natus error sit voluptatem accusantium dolore mque laudantium aut odit aut fugit, sed quia consequ</div><span class="btn">READ MORE</span></div>
</div>
<div class="abs card" style="left:462px;top:1253px;height:412px">
  <div class="shot" role="img" aria-label="Screenshot of a listed business website with workspace photo" style="background:linear-gradient(180deg,#6a8fb3 0 68%,#f3f3f3 68% 84%,#2b2b2b 84%)"></div>
  <div class="card-body"><div class="card-title">LOREM IPSUM IS SIMPLY DUMMY</div><div class="card-text">Sed ut perspiciatis unde omnis iste natus error sit voluptatem accusantium dolore mque laudantium aut odit aut fugit, sed quia consequ</div><span class="btn">READ MORE</span></div>
</div>
<div class="abs card" style="left:765px;top:1253px;height:412px">
  <div class="shot" role="img" aria-label="Screenshot of a listed business website with dark green header" style="background:linear-gradient(180deg,#2d3f3c 0 55%,#eef1f0 55% 90%,#7a2d6c 90%)"></div>
  <div class="card-body"><div class="card-title">LOREM IPSUM IS SIMPLY DUMMY</div><div class="card-text">Sed ut perspiciatis unde omnis iste natus error sit voluptatem accusantium dolore mque laudantium aut odit aut fugit, sed quia consequ</div><span class="btn">READ MORE</span></div>
</div>

<div class="abs view-all">VIEW ALL ENTREPRENEURS</div>

<!-- welcome -->
<div class="abs welcome-kicker">WELCOME TO</div>
<h2 class="abs welcome-name">VELMORA TRADE HUB</h2>
<div class="abs rule" style="top:1962px"></div>
<p class="abs welcome-text">At vero eos et accusamus et iusto odio dignissimos ducimus qui blanditiis praesentium voluptatum deleniti atque corrupti quos dolores et quas molestias excepturi sint occaecati cupiditate non provident, similique sunt in culpa qui officia deserunt mollitia animi, id est laborum et dolorum fuga. Et harum quidem rerum facilis est</p>

<div class="abs feature" style="left:194px;top:2188px">
  <svg width="56" height="56" viewBox="0 0 56 56"><circle cx="28" cy="28" r="26" fill="none" stroke="#3176b5" stroke-width="2"/><path d="M18 31v-4a10 10 0 0 1 20 0v4" fill="none" stroke="#3176b5" stroke-width="2.5"/><rect x="16" y="29" width="5" height="8" rx="2" fill="#3176b5"/><rect x="35" y="29" width="5" height="8" rx="2" fill="#3176b5"/></svg>
  <div><div class="feature-title">Get Support</div><div class="feature-text">At vero eos et accusamus et iusto odio dignissimos</div></div>
</div>
<div class="abs feature" style="left:484px;top:2188px">
  <svg width="56" height="56" viewBox="0 0 56 56"><circle cx="28" cy="28" r="26" fill="none" stroke="#3176b5" stroke-width="2"/><path d="M22 26v-4a6 6 0 0 1 12 0v4" fill="none" stroke="#3176b5" stroke-width="2.5"/><rect x="19" y="26" width="18" height="13" rx="2" fill="#3176b5"/></svg>
  <div><div class="feature-title">Secure Search</div><div class="feature-text">At vero eos et accusamus et iusto odio dignissimos</div></div>
</div>
<div class="abs feature" style="left:776px;top:2188px">
  <svg width="56" height="56" viewBox="0 0 56 56"><circle cx="28" cy="28" r="26" fill="none" stroke="#3176b5" stroke-width="2"/><path d="M21 16h10l6 6v18H21z" fill="#3176b5"/><path d="M31 16v6h6" fill="#fff" opacity=".5"/></svg>
  <div><div class="feature-title">Best Information</div><div class="feature-text">At vero eos et accusamus et iusto odio dignissimos</div></div>
</div>

<!-- how it works -->
<div class="abs steps-band"></div>
<h2 class="abs heading" style="top:2413px">HOW IT WORKS</h2>
<div class="abs rule" style="top:2466px"></div>

<div class="abs step" style="left:168px;top:2560px">
  <div class="step-art" role="img" aria-label="Illustration of a person at a desk searching"></div>
  <div class="step-title">Search Entrepreneurs</div>
  <div class="step-text">At vero eos et accusamus et iusto odio dignissimos ducimus qui blanditiis praesentium voluptatum</div>
  <div class="step-num">01</div>
</div>
<div class="abs step-divider" style="left:459px"></div>
<div class="abs step" style="left:451px;top:2560px">
  <div class="step-art" role="img" aria-label="Illustration of a profile information screen"></div>
  <div class="step-title">Show information</div>
  <div class="step-text">At vero eos et accusamus et iusto odio dignissimos ducimus qui blanditiis praesentium voluptatum</div>
  <div class="step-num">02</div>
</div>
<div class="abs step-divider" style="left:757px"></div>
<div class="abs step" style="left:758px;top:2560px">
  <div class="step-art" role="img" aria-label="Illustration of a scroll listing entrepreneurs"></div>
  <div class="step-title">View list of Entrepreneurs</div>
  <div class="step-text">At vero eos et accusamus et iusto odio dignissimos ducimus qui blanditiis praesentium voluptatum</div>
  <div class="step-num">03</div>
</div>

<!-- posts -->
<h2 class="abs heading" style="top:2939px">LATEST POSTS</h2>
<div class="abs rule" style="top:2992px"></div>

<div class="abs post" style="left:138px;top:3085px">
  <div class="shot" role="img" aria-label="Screenshot of a developer blog post page" style="background:linear-gradient(180deg,#f4f4f4 0 8%,#1a1a1a 8% 50%,#f7f7f7 50%)"></div>
  <div class="card-body"><div class="card-title">LOREM IPSUM IS SIMPLY DUMMY</div><div class="card-text">Sed ut perspiciatis unde omnis iste natus error sit voluptatem accusantium dolore mque laudantium aut odit aut fugit, sed quia consequ</div><span class="btn">READ MORE</span></div>
</div>
<div class="abs post" style="left:457px;top:3085px">
  <div class="shot" role="img" aria-label="Screenshot of an event post with purple banner" style="background:linear-gradient(180deg,#222 0 10%,#7a1f7f 10% 70%,#f3f3f3 70%)"></div>
  <div class="card-body"><div class="card-title">LOREM IPSUM IS SIMPLY DUMMY</div><div class="card-text">Sed ut perspiciatis unde omnis iste natus error sit voluptatem accusantium dolore mque laudantium aut odit aut fugit, sed quia consequ</div><span class="btn">READ MORE</span></div>
</div>
<div class="abs post" style="left:773px;top:3085px">
  <div class="shot" role="img" aria-label="Screenshot of a digital transformation article with a train photo" style="background:linear-gradient(160deg,#2f8fa8 0%,#1d4f7a 55%,#c74b3a 100%)"></div>
  <div class="card-body"><div class="card-title">LOREM IPSUM IS SIMPLY DUMMY</div><div class="card-text">Sed ut perspiciatis unde omnis iste natus error sit voluptatem accusantium dolore mque laudantium aut odit aut fugit, sed quia consequ</div><span class="btn">READ MORE</span></div>
</div>

<!-- footer -->
<footer class="abs footer">
  <div class="abs f-brand">VELMORA TRADE HUB</div>

  <div class="abs f-head" style="left:475px;top:73px">CONTACT US</div>
  <div class="abs f-row" style="left:475px;top:105px">
    <svg width="10" height="14" viewBox="0 0 10 14"><path d="M5 0a5 5 0 0 1 5 5c0 4-5 9-5 9S0 9 0 5a5 5 0 0 1 5-5z" fill="#fff"/><circle cx="5" cy="5" r="2" fill="#3176b5"/></svg>
    <div>118 Harbor Lane<br>Maplewood, OR 97015</div>
  </div>
  <div class="abs f-row" style="left:475px;top:160px">
    <svg width="10" height="12" viewBox="0 0 10 12"><path d="M1 0h3l1 3-2 1a7 7 0 0 0 3 4l1-2 3 1v3c0 1-1 2-2 2A9 9 0 0 1 0 2c0-1 0-2 1-2z" fill="#fff"/></svg>
    <div>555.010.4821</div>
  </div>
  <div class="abs f-row" style="left:475px;top:196px">
    <svg width="12" height="10" viewBox="0 0 12 10"><rect width="12" height="10" fill="#fff"/><path d="M0 0l6 5 6-5" fill="none" stroke="#3176b5" stroke-width="1.2"/></svg>
    <div>info@velmoratradehub.com</div>
  </div>

  <div class="abs f-head" style="left:733px;top:73px">MENU</div>
  <div class="abs f-menu" style="left:733px;top:104px">Home<br>About Us<br>Services<br>Entrepreneurs<br>Blog<br>Contact Us</div>

  <div class="abs f-head" style="left:935px;top:73px">CONNECT WITH US</div>
  <div class="abs f-social" style="left:935px;top:100px"><span class="dot"></span>Newsfeed</div>
  <div class="abs f-social" style="left:935px;top:140px"><span class="dot"></span>Updates</div>
  <div class="abs f-social" style="left:935px;top:180px"><span class="dot"></span>Network</div>

  <div class="abs f-line"></div>
  <div class="abs copy">Copyrights @ 2018 All Rights Reserved</div>
</footer>

</body>
</html>
```